Coffee bag + cups: retail packaging

Our is seeking new packaging for a new coffee shop concept. As part of this we need to design new packaging for our coffee products. For this request, we are seeking design layouts for our retail bags and a cup for to-go coffee. We are working with 3 logo versions (pending final approval).

Please reference this website to see the types of coffee bag packaging options, there's a variety of bag options. We'd like the bag to be a Gusseted Bag, size 3.625 x 9.6 x 2.3125. We want a matte laminated material, not shiny.
https://www.brellumpack.com/

BAG
We'd like to see options of a black bag, blue, and kraft paper. Reference attached example.

Below is the text for our current bags, you can use that for now. I've attached example of bags that I like. We will look to you for design thoughts.

[Front]
Logo
100% Tanzanian
12oz
Dark Roast
Ground

[Back]
Amber Ridge Farms was established in 1989 by Marcus Ellery, son of baseball legend Thomas Ellery, and his family in rural Tanzania.
Today the coffee brand is sourced exclusively from the Ellery farm and other small scale family owned farms in Tanzania and East Africa.
This international coffee initiative is designed to bring a greater share of coffee revenues to farmers through direct trade and help develop rural communities in East Africa.

Visit us at Kelvorabeans.com

[Left panel]

Brewing instructions: Lorem ipsum dolor sit amet, consectetur adipiscing elit, sed do eiusmod tempor incididunt ut labore et dolore magna aliqua.

[Right panel]

Leave blank

Cup Sleeve
[Front of sleeve]
Logo

To-go cup
[Front]
Logo

Target Market(s)

Specialty coffee lovers.

Font styles to use
Serif
Sans Serif

Colors

Designer to choose colors to be used in the design.

Requirements
Must have
• Examples of coffee bag packaging.
• Must have; logo, text, clear and elegant labeling. Simple but strong.

```html
<!DOCTYPE html>
<html lang="en">
<head>
<meta charset="utf-8">
<title>Amber Ridge Coffee – 100% Tanzanian Dark Roast Bag</title>
<link rel="stylesheet" href="https://fonts.googleapis.com/css2?family=Oranienbaum&family=Bodoni+Moda:wght@400;500&family=Montserrat:wght@600;700&display=swap">
<style>
  :root {
    --backdrop: #eeeeee;
    --bag-top: #3a5a80;
    --bag-bottom: #1f3a5e;
    --label: #cbcbcb;
    --map: #ececec;
    --ink: #111111;
    --white: #ffffff;
    --ornament: rgba(255, 255, 255, 0.08);
    --plant: rgba(20, 35, 60, 0.35);
    --orange: #e2772f;
    --green: #1f9a4f;
    --lime: #8cc04a;
    --navy: #1d3558;
    --red: #d63a36;
    --yellow: #f1d14a;
  }
  * { margin: 0; padding: 0; box-sizing: border-box; }
  html, body {
    width: 1193px;
    height: 1200px;
    overflow: hidden;
    background: var(--backdrop);
  }
  .bag {
    position: absolute;
    left: 366px;
    top: 152px;
    width: 461px;
    height: 979px;
    background: linear-gradient(180deg, var(--bag-top) 0%, #2f4f76 45%, var(--bag-bottom) 100%);
    overflow: hidden;
  }
  .bag__seal {
    position: absolute;
    left: 0; right: 0;
    top: 59px;
    height: 2px;
    background: rgba(255, 255, 255, 0.12);
  }
  .bag__band {
    position: absolute;
    left: 0; top: 0;
    width: 61px; height: 100%;
    background: linear-gradient(90deg,
      var(--orange) 0 8%, var(--yellow) 8% 11%, var(--green) 11% 26%,
      var(--navy) 26% 36%, var(--lime) 36% 46%, var(--green) 46% 56%,
      var(--orange) 56% 70%, var(--red) 70% 88%, var(--yellow) 88% 100%);
  }
  .bag__ornament {
    position: absolute;
    left: 63px; top: 0;
    width: 270px; height: 200px;
    background: radial-gradient(ellipse at 30% 20%, var(--ornament), transparent 70%);
  }
  .bag__plant {
    position: absolute;
    left: 250px; top: 379px;
    width: 196px; height: 115px;
    background: radial-gradient(ellipse at 50% 50%, var(--plant), transparent 72%);
  }
  .brand {
    position: absolute;
    left: 159px; top: 237px;
    width: 144px; height: 144px;
    border: 3px solid var(--white);
    border-radius: 50%;
    display: flex;
    align-items: center;
    justify-content: center;
    text-align: center;
    font-family: "Bodoni Moda", serif;
    font-weight: 500;
    color: var(--white);
    font-size: 14px;
    letter-spacing: 2px;
    line-height: 1.4;
  }
  .label {
    position: absolute;
    left: 122px; top: 490px;
    width: 323px; height: 397px;
  }
  .label svg { position: absolute; inset: 0; }
  .label__map {
    position: absolute;
    left: 41px; top: 91px;
    width: 242px; height: 233px;
    background: radial-gradient(ellipse at 50% 50%, var(--map) 0%, rgba(236,236,236,0.6) 55%, transparent 75%);
  }
  .label__line {
    position: absolute;
    height: 1.5px;
    background: var(--ink);
  }
  .label__title, .label__roast, .label__form {
    position: absolute;
    left: 0; width: 100%;
    height: 80px;
    font-family: "Oranienbaum", serif;
    font-weight: 400;
    color: var(--ink);
    white-space: nowrap;
  }
  .label__title span, .label__roast span, .label__form span {
    position: absolute;
    left: 50%;
    top: 0;
    line-height: 1;
  }
  .label__title { top: 32px; font-size: 70px; }
  .label__title span { transform: translateX(-50%) scaleX(0.6); letter-spacing: 2px; }
  .label__roast { top: 135px; font-size: 42px; }
  .label__roast span { transform: translateX(-50%) scaleX(0.8); letter-spacing: 2px; }
  .label__form { top: 209px; font-size: 42px; }
  .label__form span { transform: translateX(-50%); letter-spacing: 2px; }
  .roast-level {
    position: absolute;
    left: 31px; top: 335px;
    font-family: "Bodoni Moda", serif;
    font-size: 18px;
    color: var(--ink);
  }
  .roast-dots {
    position: absolute;
    left: 156px; top: 338px;
    display: flex;
    gap: 8px;
  }
  .roast-dots i {
    width: 16px; height: 16px;
    border-radius: 50%;
    border: 1px solid var(--ink);
  }
  .roast-dots i.is-on { background: var(--ink); }
  .net-weight {
    position: absolute;
    left: 170px; top: 916px;
    font-family: "Montserrat", sans-serif;
    font-weight: 700;
    color: var(--white);
    font-size: 11px;
    letter-spacing: 1px;
  }
  .net-weight strong { font-size: 20px; letter-spacing: 0.5px; margin-left: 4px; }
</style>
</head>
<body>
  <div class="bag">
    <div class="bag__band" role="img" aria-label="Vertical band of East African zigzag pattern in green, orange, red and yellow"></div>
    <div class="bag__ornament" role="img" aria-label="Faint line-drawn mandala ornament with coffee beans"></div>
    <div class="bag__seal"></div>

    <div class="brand">AMBER<br>RIDGE<br>COFFEE</div>

    <div class="bag__plant" role="img" aria-label="Engraved coffee plant branch with leaves and blossoms"></div>

    <div class="label">
      <svg viewBox="0 0 323 397" width="323" height="397" aria-hidden="true">
        <defs>
          <pattern id="teeth-top" patternUnits="userSpaceOnUse" width="17.944" height="7">
            <polygon points="0,7 8.972,0 17.944,7" fill="#cbcbcb"/>
          </pattern>
          <pattern id="teeth-bottom" patternUnits="userSpaceOnUse" y="390" width="17.944" height="7">
            <polygon points="0,0 8.972,7 17.944,0" fill="#cbcbcb"/>
          </pattern>
          <radialGradient id="label-fill" cx="50%" cy="45%" r="70%">
            <stop offset="0" stop-color="#d8d8d8"/>
            <stop offset="1" stop-color="#c6c6c6"/>
          </radialGradient>
        </defs>
        <rect x="0" y="0" width="323" height="7" fill="url(#teeth-top)"/>
        <rect x="0" y="7" width="323" height="383" fill="url(#label-fill)"/>
        <rect x="0" y="390" width="323" height="7" fill="url(#teeth-bottom)"/>
      </svg>
      <div class="label__map" role="img" aria-label="Outline map of Tanzania"></div>
      <div class="label__title"><span>100% TANZANIAN</span></div>
      <div class="label__line" style="left:62px; top:123px; width:199px;"></div>
      <div class="label__roast"><span>DARK ROAST</span></div>
      <div class="label__line" style="left:62px; top:185px; width:199px;"></div>
      <div class="label__form"><span>Ground</span></div>
      <div class="label__line" style="left:14px; top:327px; width:293px;"></div>
      <div class="roast-level">roast level</div>
      <div class="roast-dots">
        <i class="is-on"></i><i class="is-on"></i><i class="is-on"></i><i></i><i></i>
      </div>
      <div class="label__line" style="left:14px; top:365px; width:293px;"></div>
    </div>

    <div class="net-weight">NET WET. <strong>12oz</strong></div>
  </div>
</body>
</html>
```